Broschüren-Design für studentischen Personaldienstleister
Gute Ideen, reibungslose Zusammenarbeit und alle Anpassungen wurden schnell umgesetzt. Besser konnte es für uns nicht laufen.
Zielgruppe
KL Talentwerk ist ein studentischer Personaldienstleister, der seit 25 Jahren die IT- und Medien-Branche im Contentmanagement (Contentpflege, Redaktion, Grafik) und Onsiteservice (Floorwalking, Help Desk und Service Points) unterstützt.
Hierbei können wir auf das Know-how unserer Studenten vertrauen, die sich in der digitalen Landschaft zu Hause fühlen. Mit ihnen ergänzen wir bestehende Teams, wenn die eigene Crew ausgelastet ist oder keiner der internen Mitarbeiter Fachkenntnisse in dem erforderlichen Bereich mitbringt.
Zu unsere Kunden zählen insbesondere das Verlagswesen (Bsp. Helmut-Fasold SE), Digitalagenturen (Bsp. VORA) und IT-Dienstleister (z.B Rechnorama AG).
Aufgabenstellung
Es soll ein 3-seitiges PDF/ erstellt werden, das NUR ONLINE versendet wird, es wird nicht gedruckt. Das Format kann frei gewählt werden, es soll modern und kreativ sein.
Zusätzlich soll ein Logo/Button entworfen werden, das auf allen Kanälen ausgespielt werden kann (jpg, png und eps.)
Für das 25-jährige-Jubiläum der Zusammenarbeit der Geschäftsführer, Gernot Wallrath und Udo Kestermann, soll ein Mailing an Bestandskunden von KL Talentwerk versendet werden. Diesem Mailing soll ein PDF-Dokument/Flyer angehängt werden. Thematisch wird im Flyer der Claim “Smart. Digital. Im Team.” umgesetzt. Zusätzlich soll das bereits vorhandene Firmenlogo ein eigenes “Jubiläumsbranding” bekommen. Dieses Logo/Button soll sowohl im PDF eingebaut werden als auch zur weiteren thematischen Nutzung auf diversen sozialen Kanälen eingesetzt werden können.
SPEZIFIKATION PDF:
Umfang: 3 Seiten
Format: Kann offen gestaltet werden. Keine Vorgabe.
Inhalt: Die 3 Seiten spiegeln unseren Claim wieder. Auf jeder Seite soll ein „Fun Facts-Kasten“ eingebaut werden, der thematisch auflockert.
Design: Bitte verwenden sie unsere CI-Farben des Logos (HKS 44 + 50% Schwarz und HKS 92K). Logo fügen wir hier ein, Bild- und Textmaterial wird von uns gestellt und nach Zuschlag dem Gewinner zugesendet für die Fertigstellung des PDFs.
Seite 1: IM TEAM
Hier geht chronologisch um die Zusammenarbeit und Entstehung von KL Talentwerk GmbH. Kennenlerngeschichte. Start der Firma in Lüneburg. Zweites Büro in Berlin., neues CEO-Team mit drittem Geschäftsführer, KL Talentwerk heute.
Seite 2: SMART
Smart steht für unsere Studierenden. Warum wir mit studentischen Teams überzeugen. Wir liefern eine Win-Win-Situation mit fairen Konditionen für beide Situationen.
Feedback von unseren Studierenden. Beispiel für eine Erfolgsgeschichte, vom Studenten bei KL Talentwerk GmbH zur leitenden Position bei einem bekannten Medienunternehmen.
S..

```html
<!DOCTYPE html>
<html lang="de">
<head>
<meta charset="utf-8">
<title>KL Talentwerk – Digital.</title>
<link rel="stylesheet" href="https://fonts.googleapis.com/css2?family=Source+Sans+3:ital,wght@0,400;0,700;0,800;1,400&display=swap">
<style>
  :root {
    --navy: #1f3a6e;
    --ink: #000000;
    --text-grey: #555555;
    --amber: #ee9e12;
    --amber-soft: rgba(238, 158, 18, 0.35);
    --white: #ffffff;
    --photo-dark: #3a3a3a;
    --photo-light: #b5b5b5;
  }
  * { margin: 0; padding: 0; box-sizing: border-box; }
  html, body { width: 848px; height: 1200px; overflow: hidden; background: var(--white); }
  body { font-family: "Source Sans 3", "Source Sans Pro", sans-serif; }
  .page { position: relative; width: 848px; height: 1200px; overflow: hidden; background: var(--white); }

  .brand {
    position: absolute; left: 48px; top: 40px;
    display: flex; align-items: center; gap: 7px;
    font-weight: 700; font-size: 14px; letter-spacing: 1.2px;
    color: var(--navy); text-transform: uppercase;
  }
  .brand-dot { width: 8px; height: 8px; border-radius: 50%; background: var(--navy); }

  .section-marker { position: absolute; left: 51px; top: 92px; width: 21px; height: 38px; background: var(--navy); }
  .section-title {
    position: absolute; left: 102px; top: 82px;
    font-weight: 700; font-size: 49px; line-height: 1; color: var(--ink); letter-spacing: -0.3px;
  }

  .hero-photo {
    position: absolute; left: 305px; top: 0; width: 543px; height: 332px;
    background: linear-gradient(135deg, var(--photo-dark) 0%, #6e6e6e 45%, var(--photo-light) 100%);
  }

  .lead {
    position: absolute; left: 51px; top: 368px; width: 490px;
    font-weight: 700; font-size: 19.5px; line-height: 22.7px; color: var(--ink);
  }

  .column { position: absolute; top: 513px; width: 240px; }
  .column-left { left: 51px; }
  .column-right { left: 306px; width: 250px; }

  .column h2 {
    font-weight: 700; font-size: 24.5px; line-height: 27px; color: var(--ink);
  }
  .column p {
    font-size: 16.2px; line-height: 27px; color: var(--text-grey);
  }
  .usp-text { margin-top: 3px; }
  .benefit-title { margin-top: 14px; }
  .benefit-text { margin-top: 1px; }
  .benefit-more { margin-top: 27px; }

  .testimonial { position: relative; margin-top: 30px; }
  .testimonial-mark {
    position: absolute; left: 28px; top: 122px;
    font-size: 250px; line-height: 1; font-weight: 400; color: var(--amber-soft);
    pointer-events: none;
  }
  .testimonial p { position: relative; font-style: italic; }

  .fact-box {
    position: absolute; left: 564px; top: 374px; width: 228px; height: 826px;
    background: var(--amber);
  }
  .fact-box h3 {
    margin: 19px 0 0 27px;
    font-weight: 700; font-size: 25px; line-height: 1; color: var(--white);
  }
</style>
</head>
<body>
<main class="page">
  <div class="brand"><span class="brand-dot"></span>KL Talentwerk</div>

  <div class="section-marker"></div>
  <h1 class="section-title">Digital.</h1>

  <div class="hero-photo" role="img" aria-label="Schwarz-Weiß-Foto: zwei junge Menschen von hinten, gemeinsam auf ein Tablet schauend"></div>

  <p class="lead">El explam quis dolut que occaero rporis as est este eium exceaquam venissimil etur as doluptatur aut mo beres num est quam serit excer<br>Uptaquam commo tempor ma essint fugiam acili-simpos parchit</p>

  <section class="column column-left">
    <h2>Unser USP</h2>
    <p class="usp-text">&nbsp;El explam quis dolut que oc-<br>caero rporis as est este eium<br>exceaquam venissimil etur as<br>doluptatur aut mo beres num est<br>quam serit excersp icimporit lam<br>vel in pe nitatium im ut verat ut<br>quia consed quoditiatem aut ea<br>velignatur rendis ra sintibus.</p>

    <h2 class="benefit-title">Kundennutzen</h2>
    <p class="benefit-text">cullor ma dolutae ctaturestio<br>id quamus acesse mos dis aut<br>moluptam et facit aut eum untur<br>renis magniminvent quis del il-<br>lissed ea pora quia por secereiur<br>reste sinctem at.</p>
    <p class="benefit-more">Utem quid esequatet ut mo-<br>luptae net laccullandi sunt.<br>Uptaquam commo tempor ma<br>essint fugiam acilisimpos par-</p>
  </section>

  <section class="column column-right">
    <h2>Das sagen unsere<br>Kunden:</h2>
    <div class="testimonial">
      <span class="testimonial-mark" aria-hidden="true">“</span>
      <p>„A cor sam exernatibus, unt mo<br>cus qui volupta nosam quam<br>voluptatquam lab id eum diorepr<br>ernatiunt iducia perum earum<br>vero quas serrupt inihiligent eum-<br>qui il il inis eat lam natiam sintior<br>emporrum sum eum nulparum<br>et dolorem volesciunt lam essin<br>et repe volese aut qui remquun<br>tibusda esenia pro expelenienis<br>ex est acessimo corerum utem<br>aut magnist voluptae occuptatet<br>doloriati nat qui odiscia quae nis<br>re ped qui aut deritibus ad ut mod<br>es eatquatiamet volupis same<br>nosam es quam as dior.“</p>
    </div>
  </section>

  <aside class="fact-box">
    <h3>Did you know?</h3>
  </aside>
</main>
</body>
</html>
```